Design a tri-fold brochure for natural vitamin C business.

We are a whole food supplement business specializing in native plant nutrition. We need a tri-fold brochure designed for our natural wholefood vitamin C product. We have developed this product from the organic wild-harvested Australian Kakadu Plum.

The brand is VO-B, and the slogan is True Nature True Health.

My market is the 30-75-year-old male and female customers concerned with a healthy lifestyle.

I would like to see designs using orange, charcoal, and gold and or the designer's own choice of colors.

This brochure is to be a bespoke upmarket design.

I like the idea of a background image like a watermark. However, please be advised that our distributors may photocopy the brochure in black and white, so I don't want the background image to overpower the text and make it difficult to read.

I will provide;
1. Brochure layout
2. Brochure wording
3. Brochure product images
4. Logo image
5. Color hex codes
6. Images pertaining to my product ingredients
7. You may use the full or crop it if you prefer. Do what you think looks best
8. You may reference the file "image-6 TZ Dawn" for an idea of the colors we have used.

- Hex color codes: charcoal (Hex: #333333) orange (Hex: #FF6600) Matte Gold (Hex: #CBAB58)
- Logo: I have attached the logo png file for you to use. Upon choosing a winner, I will supply the logo as eps or ai files for the designer to apply to the final design. There will be two changes to the logo.
a) Change the color from orange to Matte Gold (Hex: #CBAB58)
b) Remove the woman's head from the logo
- You must supply a finished mock-up of the brochure.
- I require all vector files and source files.

```html
<!DOCTYPE html>
<html lang="en">
<head>
<meta charset="utf-8">
<title>VO-B Tri-fold Brochure</title>
<link href="https://fonts.googleapis.com/css2?family=Montserrat:wght@400;600;700;800&family=Open+Sans:wght@400;600&display=swap" rel="stylesheet">
<style>
:root{
  --charcoal:#333333;
  --charcoal-deep:#262626;
  --orange:#FF6600;
  --gold:#CBAB58;
  --gold-light:#E3CD8E;
  --gold-dark:#A8873A;
  --paper:#FFFFFF;
  --ink:#4a4a4a;
  --stage:#E4E4E2;
  --leaf-dark:#3F5A22;
}
*{box-sizing:border-box;margin:0;padding:0}
html,body{width:1200px;height:2400px;overflow:hidden}
body{background:var(--stage);font-family:"Open Sans",Arial,sans-serif;color:var(--ink);position:relative}
.spread{position:absolute;left:45px;width:1110px;height:1000px;display:flex;box-shadow:0 6px 24px rgba(0,0,0,.18)}
.spread--outside{top:120px}
.spread--inside{top:1280px}
.panel{width:370px;height:1000px;position:relative;overflow:hidden;background:var(--paper)}
.panel + .panel{border-left:1px solid rgba(0,0,0,.06)}
.photo{position:absolute;display:block}
h2.section-title{font-family:"Montserrat",Arial,sans-serif;font-weight:700;font-size:22px;letter-spacing:.5px;text-transform:uppercase;color:var(--gold-dark);line-height:1.2}
.rule{width:60px;height:3px;background:var(--orange);margin:12px 0 18px}
p.body-copy{font-size:14px;line-height:1.65}
.btn{display:inline-block;font-family:"Montserrat",Arial,sans-serif;font-weight:700;font-size:14px;text-transform:uppercase;letter-spacing:1px;background:var(--gold);color:var(--charcoal-deep);padding:11px 30px;border-radius:22px}

/* brand name: plain text in the body font, one colour, one weight */
.brand-name{display:flex;align-items:center;gap:12px;font-family:"Open Sans",Arial,sans-serif;font-weight:600;color:var(--charcoal);letter-spacing:4px}
.brand-name__mark{width:14px;height:14px;background:var(--charcoal);flex:none}
.tagline{font-family:"Montserrat",Arial,sans-serif;font-size:12px;letter-spacing:3px;text-transform:uppercase;color:var(--gold)}

/* panel A: why */
.why{padding:56px 36px 0}
.why-list{list-style:none;margin-top:6px}
.why-list li{font-size:14px;line-height:1.5;padding:9px 0 9px 22px;position:relative;border-bottom:1px solid #eee}
.why-list li::before{content:"";position:absolute;left:0;top:15px;width:9px;height:9px;background:var(--gold);border-radius:50%}
.why .photo{left:0;bottom:0;width:370px;height:330px;background:linear-gradient(160deg,#8fae4c,var(--leaf-dark))}
.why .photo-curve{position:absolute;left:0;bottom:300px;width:370px;height:60px}

/* panel B: about / back */
.about{background:linear-gradient(170deg,var(--gold-light),var(--gold) 55%,var(--gold-dark))}
.about__top{padding:58px 36px 0;text-align:center}
.about__top .brand-name{justify-content:center;font-size:30px;color:var(--charcoal-deep)}
.about__top .brand-name__mark{background:var(--charcoal-deep)}
.about__heading{font-family:"Montserrat",Arial,sans-serif;font-weight:700;font-size:18px;text-transform:uppercase;color:var(--charcoal-deep);margin:38px 0 12px}
.about p.body-copy{color:var(--charcoal-deep)}
.about .photo{left:85px;top:470px;width:200px;height:200px;border-radius:50%;border:6px solid var(--paper);background:radial-gradient(circle at 40% 40%,#a7c05f,var(--leaf-dark))}
.about__contact{position:absolute;left:0;bottom:0;width:370px;height:280px;background:var(--charcoal);padding:44px 40px 0}
.contact-line{display:flex;align-items:center;gap:14px;color:#e8e8e8;font-size:15px;margin-bottom:18px}
.contact-line svg{flex:none}
.about__contact .btn{margin-top:10px}

/* panel C: cover */
.cover__head{height:210px;display:flex;align-items:center;justify-content:center}
.cover__head .brand-name{font-size:40px}
.cover__arc{position:absolute;left:0;top:196px;width:370px;height:60px}
.cover .photo{left:0;top:230px;width:370px;height:470px;background:linear-gradient(170deg,#b9c98a,#7f9a45 45%,#5a4a2e)}
.cover .product{left:190px;top:520px;width:165px;height:150px;border-radius:6px;background:linear-gradient(180deg,#f4f1ea,#d9d2c0)}
.cover__band{position:absolute;left:0;bottom:0;width:370px;height:300px;background:var(--charcoal);text-align:center;padding:40px 34px 0}
.cover__band .tagline{margin-bottom:16px}
.cover__band h1{font-family:"Montserrat",Arial,sans-serif;font-weight:800;font-size:30px;line-height:1.2;text-transform:uppercase;color:var(--gold)}
.cover__band .btn{margin-top:26px}

/* panel D: kakadu plum */
.plum{padding:56px 36px 0}
.chart{margin-top:26px}
.chart__title{font-family:"Montserrat",Arial,sans-serif;font-weight:600;font-size:13px;text-transform:uppercase;letter-spacing:1px;color:var(--charcoal);margin-bottom:8px}
.plum .photo{left:0;bottom:0;width:370px;height:300px;background:linear-gradient(160deg,#7a5a40,#a9b866 55%,#5b7a30)}

/* panel E: product */
.product-panel{background:var(--charcoal);padding:56px 36px 0}
.product-panel h2.section-title{color:var(--gold)}
.product-panel p.body-copy{color:#dcdcdc}
.product-panel .photo{position:relative;margin:26px 0;width:298px;height:230px;border-radius:6px;background:linear-gradient(180deg,#f3f0e8,#cfc6b0)}
.product-panel .btn{margin-top:26px}

/* panel F: benefits */
.benefits .photo--top{left:0;top:0;width:370px;height:330px;background:radial-gradient(circle at 45% 45%,#b7c86e,#6f8a37 60%,#3d3a26)}
.benefits__arc{position:absolute;left:0;top:290px;width:370px;height:60px}
.benefits__body{position:absolute;top:380px;left:36px;right:36px}
.tick-list{list-style:none}
.tick-list li{display:flex;align-items:center;gap:12px;font-size:15px;padding:8px 0}
.benefits__note{margin-top:14px}
.benefits__row{position:absolute;left:36px;right:36px;bottom:50px;display:flex;gap:14px}
.benefits__row .photo{position:relative;flex:1;height:130px;border-radius:6px;background:linear-gradient(160deg,#c6d48a,#7f9a45)}
</style>
</head>
<body>

<section class="spread spread--outside">
  <article class="panel why">
    <h2 class="section-title">Why VO-B Vitamin C</h2>
    <div class="rule"></div>
    <ul class="why-list">
      <li>Whole food vitamin C from wild fruit</li>
      <li>Certified organic, wild harvested</li>
      <li>No synthetic fillers or additives</li>
      <li>Supports natural immune health</li>
      <li>Rich in antioxidants and polyphenols</li>
      <li>Gentle on the stomach</li>
      <li>Sourced from Northern Australia</li>
      <li>Made for everyday wellbeing</li>
    </ul>
    <div class="photo" role="img" aria-label="Kakadu plum tree branch with green leaves and fruit"></div>
    <svg class="photo-curve" viewBox="0 0 370 60" preserveAspectRatio="none" aria-hidden="true">
      <path d="M0 0 Q185 70 370 10 L370 0 Z" fill="#fff"/>
      <path d="M0 4 Q185 74 370 14" fill="none" stroke="#CBAB58" stroke-width="3"/>
    </svg>
  </article>

  <article class="panel about">
    <div class="about__top">
      <div class="brand-name"><span class="brand-name__mark"></span>VO-B</div>
      <div class="about__heading">Native Plant Nutrition</div>
      <p class="body-copy">We are a whole food supplement business specialising in native plant nutrition, bringing the power of Australian bush foods to your daily routine.</p>
    </div>
    <div class="photo" role="img" aria-label="Close-up of green Kakadu plums on the branch"></div>
    <div class="about__contact">
      <div class="contact-line">
        <svg width="22" height="22" viewBox="0 0 24 24" aria-hidden="true"><path fill="#CBAB58" d="M6.6 10.8a15 15 0 006.6 6.6l2.2-2.2a1 1 0 011-.25 11.4 11.4 0 003.6.57 1 1 0 011 1V20a1 1 0 01-1 1A17 17 0 013 4a1 1 0 011-1h3.5a1 1 0 011 1c0 1.25.2 2.45.57 3.57a1 1 0 01-.25 1z"/></svg>
        1300 555 014
      </div>
      <div class="contact-line">
        <svg width="22" height="22" viewBox="0 0 24 24" aria-hidden="true"><rect x="2" y="5" width="20" height="14" rx="2" fill="none" stroke="#CBAB58" stroke-width="2"/><path d="M3 6l9 7 9-7" fill="none" stroke="#CBAB58" stroke-width="2"/></svg>
        hello@vo-b.example
      </div>
      <div class="contact-line">
        <svg width="22" height="22" viewBox="0 0 24 24" aria-hidden="true"><circle cx="12" cy="12" r="9" fill="none" stroke="#CBAB58" stroke-width="2"/><path d="M3 12h18M12 3c3 3 3 15 0 18M12 3c-3 3-3 15 0 18" fill="none" stroke="#CBAB58" stroke-width="1.6"/></svg>
        www.vo-b.example
      </div>
      <span class="btn">Shop Online</span>
    </div>
  </article>

  <article class="panel cover">
    <div class="cover__head">
      <div class="brand-name"><span class="brand-name__mark"></span>VO-B</div>
    </div>
    <div class="photo" role="img" aria-label="Ripe Kakadu plums hanging on a branch against soft green foliage"></div>
    <svg class="cover__arc" viewBox="0 0 370 60" preserveAspectRatio="none" aria-hidden="true">
      <path d="M0 34 Q185 -10 370 40 L370 0 L0 0 Z" fill="#fff"/>
      <path d="M0 34 Q185 -10 370 40" fill="none" stroke="#CBAB58" stroke-width="3"/>
    </svg>
    <div class="photo product" role="img" aria-label="Group of VO-B vitamin C supplement bottles"></div>
    <div class="cover__band">
      <div class="tagline">True Nature True Health</div>
      <h1>Nature's Richest Source of Vitamin C</h1>
      <span class="btn">Order Today</span>
    </div>
  </article>
</section>

<section class="spread spread--inside">
  <article class="panel plum">
    <h2 class="section-title">The Kakadu Plum</h2>
    <div class="rule"></div>
    <p class="body-copy">Wild harvested across the Top End, the Kakadu Plum holds more natural vitamin C than any other fruit known on Earth.</p>
    <div class="chart">
      <div class="chart__title">Vitamin C per 100g</div>
      <svg width="298" height="220" viewBox="0 0 298 220" role="img" aria-label="Bar chart comparing vitamin C content of fruits">
        <line x1="20" y1="190" x2="290" y2="190" stroke="#bbb" stroke-width="1"/>
        <rect x="34" y="172" width="44" height="18" fill="#E3CD8E"/>
        <rect x="100" y="168" width="44" height="22" fill="#CBAB58"/>
        <rect x="166" y="160" width="44" height="30" fill="#E0903A"/>
        <rect x="232" y="20" width="44" height="170" fill="#FF6600"/>
        <g font-family="Open Sans, Arial, sans-serif" font-size="12" fill="#4a4a4a" text-anchor="middle">
          <text x="56" y="208">Orange</text>
          <text x="122" y="208">Lemon</text>
          <text x="188" y="208">Kiwi</text>
          <text x="254" y="208">Kakadu</text>
        </g>
      </svg>
    </div>
    <div class="photo" role="img" aria-label="Hands holding freshly picked green Kakadu plums"></div>
  </article>

  <article class="panel product-panel">
    <h2 class="section-title">Pure Whole Food Goodness</h2>
    <div class="rule"></div>
    <p class="body-copy">Each capsule delivers vitamin C exactly as nature made it, together with the fruit's own cofactors for better absorption.</p>
    <div class="photo" role="img" aria-label="Three VO-B vitamin C bottles side by side"></div>
    <p class="body-copy">Take one capsule daily with food.</p>
    <span class="btn">Learn More</span>
  </article>

  <article class="panel benefits">
    <div class="photo photo--top" role="img" aria-label="Pile of fresh green Kakadu plums"></div>
    <svg class="benefits__arc" viewBox="0 0 370 60" preserveAspectRatio="none" aria-hidden="true">
      <path d="M0 40 Q185 -6 370 30 L370 60 L0 60 Z" fill="#fff"/>
      <path d="M0 40 Q185 -6 370 30" fill="none" stroke="#CBAB58" stroke-width="3"/>
    </svg>
    <div class="benefits__body">
      <h2 class="section-title">Benefits</h2>
      <div class="rule"></div>
      <ul class="tick-list">
        <li><svg width="18" height="18" viewBox="0 0 24 24" aria-hidden="true"><circle cx="12" cy="12" r="11" fill="#CBAB58"/><path d="M7 12l3.5 3.5L17 9" fill="none" stroke="#fff" stroke-width="2.4"/></svg>Immune system support</li>
        <li><svg width="18" height="18" viewBox="0 0 24 24" aria-hidden="true"><circle cx="12" cy="12" r="11" fill="#CBAB58"/><path d="M7 12l3.5 3.5L17 9" fill="none" stroke="#fff" stroke-width="2.4"/></svg>Healthy skin and collagen</li>
        <li><svg width="18" height="18" viewBox="0 0 24 24" aria-hidden="true"><circle cx="12" cy="12" r="11" fill="#CBAB58"/><path d="M7 12l3.5 3.5L17 9" fill="none" stroke="#fff" stroke-width="2.4"/></svg>Natural energy levels</li>
        <li><svg width="18" height="18" viewBox="0 0 24 24" aria-hidden="true"><circle cx="12" cy="12" r="11" fill="#CBAB58"/><path d="M7 12l3.5 3.5L17 9" fill="none" stroke="#fff" stroke-width="2.4"/></svg>Antioxidant protection</li>
      </ul>
      <p class="body-copy benefits__note">Feel the difference of true nature.</p>
    </div>
    <div class="benefits__row">
      <div class="photo" role="img" aria-label="Single Kakadu plums on a light surface"></div>
      <div class="photo" role="img" aria-label="Sliced Kakadu plum showing the flesh"></div>
    </div>
  </article>
</section>

</body>
</html>
```